Quickgate Bailbonds Outdoor lighted sign

I am getting a sign outside of my office building that lights up at night. The size of the sign is 7'×11"3/4 width
3'×11"3/4 height

I need to design how I want the sign to look. I want it to be very catchy so people who pass by in their cars will remember the sign. Especially the business name. I want the sign to be very memorable. The business name is important for people to remember as we have several competitors. I would love something fun and eye catching. At this business all women work here so we are not sure if we want something fun and spicy or more professional. We aren’t sure which one that we want and can’t wait to see the designs! I do not have a logo.

Target Market(s)

To catch people’s eye. Exposure

Industry/Entity Type

Bailbonds

Font styles to use
Serif

Requirements
Must have
• Quickgate Bailbonds 555-318-7064
Nice to have
• Fast Release 24 Hours Any County

```html
<!DOCTYPE html>
<html lang="en">
<head>
<meta charset="utf-8">
<title>Quickgate Bailbonds – Lighted Sign</title>
<link rel="stylesheet" href="https://fonts.googleapis.com/css2?family=Anton&family=Bodoni+Moda:wght@500&display=swap">
<style>
  :root {
    --page-bg: #e9ecef;
    --frame-silver: #c4c6c8;
    --frame-shadow: #8d8f92;
    --gold-deep: #c19f22;
    --gold-light: #eee2b0;
    --ink: #0b0b0b;
    --paper: #ffffff;
    --alarm-red: #c92e22;
    --cell-dark: #3a3431;
  }
  * { box-sizing: border-box; margin: 0; padding: 0; }
  html, body {
    width: 1200px; height: 1019px; overflow: hidden;
    background: var(--page-bg);
  }
  .canvas {
    position: relative; width: 1200px; height: 1019px;
    display: flex; align-items: center; justify-content: center;
  }
  .sign-frame {
    width: 1140px; height: 580px; padding: 12px;
    background: linear-gradient(180deg, var(--frame-silver), var(--frame-shadow));
    border-radius: 4px;
    box-shadow: 0 10px 24px rgba(0,0,0,.18);
  }
  .sign-face {
    position: relative; width: 100%; height: 100%;
    background: linear-gradient(100deg,
      var(--gold-light) 0%, var(--gold-deep) 18%, var(--gold-deep) 30%,
      var(--gold-light) 45%, var(--gold-deep) 62%, var(--gold-deep) 78%, var(--gold-light) 100%);
    border: 3px solid #f4ecc8;
    overflow: hidden;
  }
  .business-name {
    position: absolute; left: 38px; top: 56px;
    width: 520px; height: 86px;
    background: var(--ink); color: var(--paper);
    font-family: "Anton", sans-serif; font-size: 56px; line-height: 86px;
    text-align: center; text-transform: uppercase; letter-spacing: 1px;
  }
  .cuffs-art {
    position: absolute; left: 48px; top: 150px; width: 470px; height: 210px;
    background: radial-gradient(ellipse at center, rgba(20,20,20,.55), rgba(20,20,20,.12) 70%, transparent);
    border-radius: 12px;
  }
  .hours-badge {
    position: absolute; left: 525px; top: 130px; width: 200px; height: 210px;
  }
  .hours-badge text { font-family: "Anton", sans-serif; fill: var(--gold-light); }
  .cell-art {
    position: absolute; left: 735px; top: 50px; width: 340px; height: 300px;
    border: 14px solid var(--ink);
    background: linear-gradient(180deg, var(--gold-deep), var(--cell-dark));
  }
  .tagline-row {
    position: absolute; left: 36px; bottom: 46px; width: 1040px;
    display: flex; align-items: baseline; gap: 24px;
  }
  .phone {
    display: flex; align-items: center; gap: 8px; flex: none;
    font-family: "Anton", sans-serif; font-size: 38px; color: var(--alarm-red);
    white-space: nowrap;
  }
  .phone-icon { width: 36px; height: 36px; flex: none; }
  .tagline {
    flex: none;
    font-family: "Bodoni Moda", serif; font-weight: 500;
    font-size: 70px; line-height: 1; color: var(--alarm-red);
    white-space: nowrap; transform: scaleX(.66); transform-origin: left bottom;
  }
</style>
</head>
<body>
<main class="canvas">
  <div class="sign-frame">
    <div class="sign-face">
      <h1 class="business-name">Quickgate Bailbonds</h1>

      <div class="cuffs-art" role="img" aria-label="Illustration of two pairs of open black handcuffs"></div>

      <svg class="hours-badge" viewBox="0 0 200 200" aria-label="24 hours">
        <polygon fill="var(--alarm-red)" points="100,0 108,22 124,3 126,26 146,11 142,34 165,24 155,45 179,41 165,60 189,62 170,76 193,84 171,92 196,100 171,108 193,116 170,124 189,138 165,140 179,159 155,155 165,176 142,166 146,189 126,174 124,197 108,178 100,200 92,178 76,197 74,174 54,189 58,166 35,176 45,155 21,159 35,140 11,138 30,124 7,116 29,108 4,100 29,92 7,84 30,76 11,62 35,60 21,41 45,45 35,24 58,34 54,11 74,26 76,3 92,22"/>
        <text x="100" y="112" text-anchor="middle" font-size="78">24</text>
        <text x="100" y="150" text-anchor="middle" font-size="30">HOURS</text>
      </svg>

      <div class="cell-art" role="img" aria-label="Illustration of three silhouetted figures behind jail bars"></div>

      <div class="tagline-row">
        <p class="phone">
          <svg class="phone-icon" viewBox="0 0 36 36" aria-hidden="true">
            <circle cx="18" cy="18" r="16" fill="none" stroke="var(--alarm-red)" stroke-width="2.5"/>
            <path d="M14 9 q-4 9 2 18 l3 -2 -3 -5 -2 1 q-2 -4 0 -8 l2 1 2 -5z" fill="var(--ink)"/>
          </svg>
          555-318-7064
        </p>
        <p class="tagline">Fast Release 24 Hours Any County</p>
      </div>
    </div>
  </div>
</main>
</body>
</html>
```